Tallbridge needs a new rocket based website

We need a new website that will be based on our rocket ship logo. We develop innovative solutions for enterprises. We would like to see a design that when the pages scroll, the rocket launches and goes from launch through a journey, similar to how we approach our customer. We would like areas for "Who are we", "What can we do", "What have we done", "How can we help". http://www.tallbridge.com.au is our current website

Target Market(s)

Government, Enterprise, Cloud

Industry/Entity Type

Software Service

Coding

Coded - Design and coding required

Number of Pages Required

2 page

Requirements
Must have
• We would like to see a design that when the pages scroll, the rocket launches and goes from launch through a journey, similar to how we approach our customer.
• Must have a home page and a detail page.
• Would like to see the logo/rocket animate in some way when you scroll through he page.

```html
<!DOCTYPE html>
<html lang="en">
<head>
<meta charset="utf-8">
<title>Tallbridge — Rocket</title>
<link href="https://fonts.googleapis.com/css2?family=Oswald:wght@500;600&family=Raleway:wght@400;500;600;700&display=swap" rel="stylesheet">
<style>
:root{
  --orange:#f0901a;
  --orange-soft:#f7a93a;
  --dark:#4b4b4d;
  --light:#f4f4f4;
  --white:#ffffff;
  --text:#6b6b6b;
  --heading:#2d2d2d;
}
*{box-sizing:border-box;margin:0;padding:0}
html,body{width:1200px;height:3564px;overflow:hidden}
body{font-family:"Raleway",Arial,sans-serif;color:var(--text);background:var(--white);position:relative}
.abs{position:absolute}
section,header,footer{position:absolute;left:0;width:1200px}

/* hero */
.hero{top:0;height:1181px;background:var(--orange);overflow:hidden}
.hero-sky{position:absolute;left:0;top:0;width:1200px;height:420px;background:linear-gradient(#3c3c3e 0%,#4d4d4f 55%,#f7a935 80%,#f0901a 100%)}
.brand{position:absolute;top:18px;left:0;width:1200px;color:var(--white);font-weight:700;font-size:30px;display:flex;justify-content:center;align-items:center;gap:10px}
.brand-dot{width:14px;height:14px;border-radius:50%;background:var(--orange);display:block}
.hero-rocket{left:535px;top:130px;width:130px;height:310px;border-radius:60px 60px 20px 20px;background:linear-gradient(#f4c14a,#e8472a)}
.hero-title{top:540px;width:1200px;text-align:center;font-family:"Oswald",sans-serif;font-weight:500;font-size:96px;letter-spacing:4px;color:var(--white);line-height:1}
.hero-sub{top:656px;left:450px;width:300px;text-align:center;white-space:nowrap;color:var(--white);font-size:13px;letter-spacing:.5px;border-top:1px solid rgba(255,255,255,.7);border-bottom:1px solid rgba(255,255,255,.7);padding:4px 0}
.hero-rule{top:772px;left:86px;width:1028px;border-top:1px solid rgba(255,255,255,.3)}

.about-rule{top:862px;left:86px;width:125px;border-top:1px solid rgba(255,255,255,.8)}
.about-title{top:880px;left:86px;font-family:"Oswald",sans-serif;font-weight:500;font-size:29px;color:var(--white);letter-spacing:1px}
.about-lead{top:934px;left:86px;width:640px;color:#3a2a10;font-weight:700;font-size:13.5px}
.about-body{top:962px;left:86px;width:640px;color:var(--white);font-size:13.5px;line-height:27px}
.about-image{left:772px;top:860px;width:345px;height:252px;background:linear-gradient(135deg,#2d4f8f,#9fbde6)}

/* side nav */
.side-nav{left:0;width:48px}
.side-nav .tab{width:48px;height:44px;background:var(--orange-soft);border-bottom:1px solid rgba(255,255,255,.35);display:flex;align-items:center;justify-content:center}
.side-label{left:0;height:42px;background:var(--orange-soft);color:var(--white);font-size:15px;font-weight:600;display:flex;align-items:center;padding-left:50px}
.side-rocket{border-radius:30px 30px 10px 10px;background:linear-gradient(#ffffff,#f08a1e)}

/* section heads */
.sec-rule{left:540px;width:120px;border-top:1px solid #e2a35a}
.sec-title{width:1200px;left:0;text-align:center;font-family:"Oswald",sans-serif;font-weight:600;font-size:32px;color:var(--heading);letter-spacing:1px}
.sec-sub{width:1200px;left:0;text-align:center;color:var(--orange);font-size:13px;font-weight:600}

/* services */
.services{top:1181px;height:428px;background:var(--light)}
.service{top:221px;width:257px;text-align:center}
.service-icon{width:72px;height:72px;margin:0 auto;border-radius:50%;background:var(--white);box-shadow:0 2px 6px rgba(0,0,0,.1);display:flex;align-items:center;justify-content:center}
.service h3{margin-top:22px;font-weight:500;font-size:18px;color:var(--heading)}
.service p{margin-top:8px;font-size:13.5px;line-height:24px;color:#7a7a7a}
.service-divider{top:221px;height:170px;border-left:1px solid #e3e3e3}

/* work */
.work{top:1609px;height:498px;background:var(--dark)}
.work .sec-title{color:var(--white)}
.work-card{top:180px;width:326px;height:247px;overflow:hidden}
.work-card .photo{width:100%;height:100%}
.work-card .caption{position:absolute;left:0;bottom:0;width:100%;height:45px;background:rgba(240,144,26,.85);color:var(--white);text-align:center;font-size:18px;line-height:45px}

/* help */
.help{top:2107px;height:697px;background:var(--light)}
.tabs{left:86px;top:193px;width:1028px;height:74px;display:flex;background:var(--white);border:1px solid #e6e6e6}
.tabs div{flex:1;display:flex;align-items:center;justify-content:center;font-size:16px;color:var(--heading)}
.tabs .muted{background:#e9e9e9}
.tabs .active{background:var(--orange);color:var(--white)}
.panel{left:86px;top:267px;width:1028px;height:361px;background:var(--white);border:1px solid #e6e6e6;border-top:none;box-shadow:0 4px 8px rgba(0,0,0,.05)}
.panel-image{left:45px;top:45px;width:385px;height:273px;background:linear-gradient(#cfe6f3,#a9cfe3);border:3px solid #e0eef6}
.panel h4{position:absolute;left:463px;top:58px;font-size:18px;font-weight:600;color:var(--heading)}
.panel p{position:absolute;left:463px;top:92px;width:530px;font-size:13.5px;line-height:23.5px;color:#666}

/* contact */
.contact{top:2804px;height:558px;background:var(--white)}
.label{font-size:16px;font-weight:500;color:var(--heading)}
.field{left:86px;width:501px;border:1px solid #e3e3e3;font-size:13px;color:#888;padding:10px 14px}
.submit{left:86px;top:446px;width:149px;height:41px;background:var(--orange);color:var(--white);font-weight:700;font-size:14px;display:flex;align-items:center;justify-content:center}
.map{left:613px;top:223px;width:501px;height:264px;border:3px solid #e4e4e4;background:linear-gradient(135deg,#e8e8e6,#d6d9dc)}

/* footer */
.site-footer{top:3362px;height:202px;background:var(--dark)}
.foot-brand{left:86px;top:40px;color:var(--white);font-weight:700;font-size:22px;display:flex;align-items:center;gap:8px}
.foot-brand .brand-dot{width:11px;height:11px}
.foot-addr{left:86px;top:74px;color:var(--white);font-size:12px;line-height:17px}
.foot-addr b{display:block;font-weight:700}
.foot-item{top:71px;display:flex;align-items:center;gap:16px;color:var(--white)}
.foot-item small{display:block;font-size:12px}
.foot-item span{display:block;font-size:18px}
.foot-follow{left:993px;top:80px;color:var(--white);font-size:12px;display:flex;align-items:center;gap:12px}
.foot-follow i{width:28px;height:28px;border-radius:50%;background:#ffffff;display:block}
.foot-rule{left:86px;top:150px;width:1028px;border-top:1px solid rgba(255,255,255,.2)}
.copyright{left:0;top:166px;width:1200px;text-align:center;color:var(--white);font-size:12px}
</style>
</head>
<body>

<header class="hero">
  <div class="hero-sky" role="img" aria-label="Night sky with stars above a band of orange clouds"></div>
  <div class="brand"><i class="brand-dot"></i>Tallbridge</div>
  <div class="abs hero-rocket" role="img" aria-label="Illustration of a rocket lifting off through clouds"></div>
  <h1 class="abs hero-title">ROCKET</h1>
  <div class="abs hero-sub">INNOVATIVE SOLUTIONS FOR ENTERPRISES</div>
  <div class="abs hero-rule"></div>

  <div class="abs about-rule"></div>
  <h2 class="abs about-title">WHO ARE WE</h2>
  <p class="abs about-lead">Lorem Ipsum is simply dummy text of the printing and typesetting industry.</p>
  <p class="abs about-body">Lorem Ipsum has been the industry's standard dummy text ever since the 1500s, when an unknown printer took a galley of type and scrambled it to make a type specimen book. It has survived not only five centuries, but also the leap into electronic typesetting, remaining essentially unchanged. It was popularised in the 1960s with the release of Lettrafix sheets containing Lorem Ipsum passages, and more recently with desktop publishing software like Quill PageSetter.</p>
  <div class="abs about-image" role="img" aria-label="Photo of city towers seen from below"></div>
</header>

<nav class="abs side-nav" style="top:945px;z-index:3">
  <div class="tab"><svg width="20" height="14" viewBox="0 0 20 14"><rect width="20" height="14" rx="1" fill="#fff"/><path d="M0 0 L10 8 L20 0" stroke="#f7a93a" stroke-width="2" fill="none"/></svg></div>
  <div class="tab"><svg width="8" height="20" viewBox="0 0 8 20"><circle cx="4" cy="3" r="2.5" fill="#fff"/><rect x="2" y="8" width="4" height="12" fill="#fff"/></svg></div>
  <div class="tab"><svg width="20" height="16" viewBox="0 0 20 16"><rect y="4" width="20" height="12" rx="2" fill="#fff"/><rect x="6" width="8" height="5" rx="1" fill="none" stroke="#fff" stroke-width="2"/></svg></div>
  <div class="tab"><svg width="18" height="18" viewBox="0 0 18 18"><circle cx="9" cy="9" r="7" fill="none" stroke="#fff" stroke-width="4" stroke-dasharray="3 2"/><circle cx="9" cy="9" r="3" fill="#fff"/></svg></div>
  <div class="tab"><svg width="20" height="16" viewBox="0 0 20 16"><circle cx="6" cy="5" r="3" fill="#fff"/><circle cx="14" cy="5" r="3" fill="#fff"/><ellipse cx="10" cy="13" rx="7" ry="3" fill="#fff"/></svg></div>
</nav>
<div class="abs side-label" style="top:1123px;width:273px;z-index:2">WHO ARE WE</div>
<div class="abs side-rocket" style="left:197px;top:1131px;width:55px;height:150px;z-index:4" role="img" aria-label="Small rocket marking the scroll position"></div>

<section class="services">
  <div class="abs sec-rule" style="top:68px"></div>
  <h2 class="abs sec-title" style="top:88px">WHAT CAN WE DO</h2>
  <p class="abs sec-sub" style="top:143px">Lorem Ipsum is simply dummy text of the printing and typesetting industry.</p>

  <div class="abs service" style="left:86px">
    <div class="service-icon"><svg width="34" height="32" viewBox="0 0 34 32"><path d="M2 10 L17 2 L32 10Z" fill="#f0901a"/><g fill="#f0901a"><rect x="5" y="12" width="4" height="13"/><rect x="12" y="12" width="4" height="13"/><rect x="19" y="12" width="4" height="13"/><rect x="26" y="12" width="4" height="13"/><rect x="2" y="27" width="30" height="4"/></g></svg></div>
    <h3>e-Parliament</h3><p>All of your Parliamentary software<br>and business process needs.</p>
  </div>
  <div class="abs service-divider" style="left:343px"></div>
  <div class="abs service" style="left:343px">
    <div class="service-icon"><svg width="36" height="24" viewBox="0 0 36 24"><path d="M8 24 A8 8 0 0 1 7 8 A10 10 0 0 1 26 6 A9 9 0 0 1 28 24Z" fill="#f0901a"/></svg></div>
    <h3>Cloud</h3><p>Office Suite Online, Migration,<br>Security, Customisations.</p>
  </div>
  <div class="abs service-divider" style="left:600px"></div>
  <div class="abs service" style="left:600px">
    <div class="service-icon"><svg width="32" height="32" viewBox="0 0 32 32"><circle cx="16" cy="5" r="3" fill="#f0901a"/><path d="M16 7 L5 30 M16 7 L27 30 M8 20 H24" stroke="#f0901a" stroke-width="3" fill="none"/></svg></div>
    <h3>Architecture and Design</h3><p>Business process design, tech-<br>-nology strategy and architecture.</p>
  </div>
  <div class="abs service-divider" style="left:857px"></div>
  <div class="abs service" style="left:857px">
    <div class="service-icon"><svg width="36" height="32" viewBox="0 0 36 32"><rect x="1" y="1" width="30" height="24" rx="2" fill="none" stroke="#f0901a" stroke-width="2"/><path d="M1 7 H31" stroke="#f0901a" stroke-width="2"/><path d="M11 11 L7 16 L11 21 M21 11 L25 16 L21 21 M17 10 L15 22" stroke="#f0901a" stroke-width="2" fill="none"/><circle cx="30" cy="26" r="5" fill="#f0901a"/></svg></div>
    <h3>Software Development</h3><p>Software development including<br>business apps, web and mobile.</p>
  </div>
</section>

<section class="work">
  <div class="abs sec-rule" style="top:68px"></div>
  <h2 class="abs sec-title" style="top:88px">WHAT WE HAVE DONE</h2>
  <p class="abs sec-sub" style="top:143px">Lorem Ipsum is simply dummy text of the printing and typesetting industry.</p>
  <div class="abs work-card" style="left:86px"><div class="photo" role="img" aria-label="Photo of a person using a digital display wall" style="background:linear-gradient(135deg,#1f3445,#6f8ea3)"></div><div class="caption">Lorem ipsum simple dummy</div></div>
  <div class="abs work-card" style="left:437px"><div class="photo" role="img" aria-label="Photo of hands on a laptop with cloud network graphics" style="background:linear-gradient(135deg,#0b5fb0,#5fb7ea)"></div><div class="caption">Contrary to popular belief</div></div>
  <div class="abs work-card" style="left:789px"><div class="photo" role="img" aria-label="Rendered cutaway of an office floor plan" style="background:linear-gradient(135deg,#c7cdd0,#8f9a9e)"></div><div class="caption">Sed ut perspiciatis unde omnis</div></div>
</section>

<section class="help">
  <div class="abs sec-rule" style="top:68px"></div>
  <h2 class="abs sec-title" style="top:88px">HOW CAN WE HELP</h2>
  <p class="abs sec-sub" style="top:143px">Lorem Ipsum is simply dummy text of the printing and typesetting industry.</p>
  <div class="abs tabs"><div>Lorem Ipsum</div><div class="muted">Contrary Popular</div><div class="active">Lorem Ipsum</div><div class="muted">Contrary Popular</div><div>Lorem Ipsum</div></div>
  <div class="abs panel">
    <div class="abs panel-image" role="img" aria-label="Illustration of cloud computing with gears and screens"></div>
    <h4>Lorem ipsum dummy text printing</h4>
    <p>Lorem Ipsum is simply dummy text of the printing and typesetting industry. Lorem Ipsum has been the industry's standard dummy text ever since the 1500s, when an unknown printer took a galley of type and scrambled it to make a type specimen book. It has survived not only five centuries, but also the leap into electronic typesetting, remaining essentially unchanged. It was popularised in the 1960s with the release of Lettrafix sheets containing Lorem Ipsum passages, and more recently with desktop publishing software like Quill PageSetter including versions of Lorem Ipsum.</p>
  </div>
</section>

<nav class="abs side-nav" style="top:2174px;z-index:3">
  <div class="tab"><svg width="20" height="14" viewBox="0 0 20 14"><rect width="20" height="14" rx="1" fill="#fff"/><path d="M0 0 L10 8 L20 0" stroke="#f7a93a" stroke-width="2" fill="none"/></svg></div>
  <div class="tab"><svg width="8" height="20" viewBox="0 0 8 20"><circle cx="4" cy="3" r="2.5" fill="#fff"/><rect x="2" y="8" width="4" height="12" fill="#fff"/></svg></div>
  <div class="tab"><svg width="20" height="16" viewBox="0 0 20 16"><rect y="4" width="20" height="12" rx="2" fill="#fff"/><rect x="6" width="8" height="5" rx="1" fill="none" stroke="#fff" stroke-width="2"/></svg></div>
  <div class="tab"><svg width="18" height="18" viewBox="0 0 18 18"><circle cx="9" cy="9" r="7" fill="none" stroke="#fff" stroke-width="4" stroke-dasharray="3 2"/><circle cx="9" cy="9" r="3" fill="#fff"/></svg></div>
  <div class="tab"><svg width="20" height="16" viewBox="0 0 20 16"><circle cx="6" cy="5" r="3" fill="#fff"/><circle cx="14" cy="5" r="3" fill="#fff"/><ellipse cx="10" cy="13" rx="7" ry="3" fill="#fff"/></svg></div>
</nav>
<div class="abs side-label" style="top:2224px;width:275px;z-index:2">HOW CAN WE HELP</div>
<div class="abs side-rocket" style="left:264px;top:2232px;width:40px;height:120px;z-index:4" role="img" aria-label="Small rocket marking the scroll position"></div>

<section class="contact">
  <div class="abs sec-rule" style="top:68px"></div>
  <h2 class="abs sec-title" style="top:88px">CONTACT US</h2>
  <p class="abs sec-sub" style="top:143px">Lorem Ipsum is simply dummy text of the printing and typesetting industry.</p>
  <div class="abs label" style="left:86px;top:190px">Contact Form</div>
  <div class="abs field" style="top:225px;height:40px">Name</div>
  <div class="abs field" style="top:285px;height:40px">Email</div>
  <div class="abs field" style="top:346px;height:78px">Message</div>
  <div class="abs submit">Submit</div>
  <div class="abs label" style="left:613px;top:190px">Find us on Map</div>
  <div class="abs map" role="img" aria-label="Street map showing the office location"></div>
</section>

<footer class="site-footer">
  <div class="abs foot-brand"><i class="brand-dot"></i>Tallbridge</div>
  <div class="abs foot-addr"><b>ADDRESS:</b>Unit 7, 48 Marlow St<br>Kenwick, SA 5071</div>
  <div class="abs foot-item" style="left:352px">
    <svg width="30" height="30" viewBox="0 0 30 30"><path d="M7 3 L12 3 L14 10 L10 13 Q13 19 18 21 L21 17 L28 19 L28 24 Q27 28 22 28 Q4 24 3 8 Q3 3 7 3Z" fill="none" stroke="#f0901a" stroke-width="2"/></svg>
    <div><small>Call us on</small><span>1300 482 117</span></div>
  </div>
  <div class="abs foot-item" style="left:641px">
    <svg width="30" height="22" viewBox="0 0 30 22"><rect x="1" y="1" width="28" height="20" fill="none" stroke="#f0901a" stroke-width="2"/><path d="M1 1 L15 12 L29 1" fill="none" stroke="#f0901a" stroke-width="2"/></svg>
    <div><small>Mail us on</small><span>hello@tallbridge.com.au</span></div>
  </div>
  <div class="abs foot-follow">Follow us on <i></i></div>
  <div class="abs foot-rule"></div>
  <div class="abs copyright">Copyright © Tallbridge 2018 &nbsp;|&nbsp; All Rights Reserved.</div>
</footer>

</body>
</html>
```